New business card/stationary for a consulting company

I am looking for a clean and very professional looking business card for my consulting company as well as corresponding stationary. I am uploading our logo. I like simple and powerful for the feel. No graphics but I am open on everything else. Below is my contact information but would like the final to be in a version I can add my employees information into and print. Thank you.

Daniel Whitcombe
dan@fernlowadvisory.com
2837 North 9th Avenue, Summit Floor, Ashgrove, Indiana 60483
www.fernlowadvisory.com

Industry/Entity Type

Consulting

Contact Information for Business Card

Daniel Whitcombe
dan@fernlowadvisory.com
www.fernlowadvisory.com

Font styles to use
Serif
Sans Serif

Requirements
Must have
• Our logo and the business card details.
Nice to have
• our website www.fernlowadvisory.com

```html
<!DOCTYPE html>
<html lang="en">
<head>
<meta charset="utf-8">
<title>Fernlow Advisory – Business Card</title>
<link href="https://fonts.googleapis.com/css2?family=Cinzel:wght@700&family=Roboto:wght@400;700&family=Questrial&display=swap" rel="stylesheet">
<style>
  :root {
    --backdrop: #e4e2de;
    --card-white: #f6f6f5;
    --navy: #02025f;
    --text-grey: #555555;
    --silver: #e2e2e6;
  }
  * { box-sizing: border-box; margin: 0; padding: 0; }
  html, body {
    width: 1200px;
    height: 960px;
    overflow: hidden;
    background: var(--backdrop);
  }
  .canvas {
    position: relative;
    width: 1200px;
    height: 960px;
  }
  .card {
    position: absolute;
    width: 600px;
    height: 343px;
    box-shadow: 0 2px 4px rgba(0,0,0,0.25);
  }
  .card-front {
    left: 302px;
    top: 129px;
    background: var(--card-white);
    text-align: center;
  }
  .card-back {
    left: 299px;
    top: 488px;
    background: var(--navy);
  }
  .brand {
    position: absolute;
    left: 0;
    right: 0;
    display: flex;
    align-items: center;
    justify-content: center;
    gap: 14px;
    font-family: "Questrial", sans-serif;
    text-transform: uppercase;
    white-space: nowrap;
  }
  .brand-square {
    display: block;
    flex: none;
  }
  .card-front .brand {
    top: 92px;
    font-size: 26px;
    letter-spacing: 1px;
    color: var(--navy);
  }
  .card-front .brand-square {
    width: 30px;
    height: 30px;
    background: var(--navy);
  }
  .holder-name {
    position: absolute;
    left: 0; right: 0;
    top: 170px;
    font-family: "Cinzel", serif;
    font-weight: 700;
    font-size: 22px;
    letter-spacing: 0.5px;
    color: var(--navy);
  }
  .contact {
    position: absolute;
    left: 0; right: 0;
    font-family: "Roboto", sans-serif;
    font-size: 14px;
    color: var(--text-grey);
    line-height: 18px;
  }
  .contact-email { top: 197px; }
  .contact-address { top: 232px; }
  .contact-web {
    top: 270px;
    font-weight: 700;
    text-transform: uppercase;
  }
  .card-back .brand {
    top: 188px;
    font-size: 32px;
    letter-spacing: 1px;
    color: var(--silver);
  }
  .card-back .brand-square {
    width: 34px;
    height: 34px;
    background: var(--silver);
  }
</style>
</head>
<body>
  <main class="canvas">
    <section class="card card-front">
      <div class="brand"><span class="brand-square"></span>Fernlow Advisory</div>
      <h1 class="holder-name">Daniel Whitcombe</h1>
      <p class="contact contact-email">dan@fernlowadvisory.com</p>
      <p class="contact contact-address">2837 North 9th Avenue<br>Summit Floor, Ashgrove, Indiana 60483</p>
      <p class="contact contact-web">www.fernlowadvisory.com</p>
    </section>
    <section class="card card-back">
      <div class="brand"><span class="brand-square"></span>Fernlow Advisory</div>
    </section>
  </main>
</body>
</html>
```